" A empresa desenvolve projetos residenciais, corporativos entre outros para público de médio/alto padrão, bem como acompanhamento/gerenciamento de obra e contam com parceiros na execução do projeto... "

```html
<!DOCTYPE html>
<html lang="pt-BR">
<head>
<meta charset="UTF-8">
<title>Crachá — Livia Prado Arquitetura e Interiores</title>
<link rel="stylesheet" href="https://fonts.googleapis.com/css2?family=Roboto:wght@400;500;700&display=swap">
<style>
  :root {
    --bg: #e8e8e8;
    --ink: #1f1f1f;
    --ink-soft: #555555;
    --card-white: #ffffff;
    --card-black: #141414;
    --stripe-light: #eeeeee;
    --stripe-dark: #262626;
    --accent: #f2c21b;
    --photo-top: #d9d2c8;
    --photo-bottom: #3a3a3a;
    --slot: #cfcfcf;
  }
  * { box-sizing: border-box; margin: 0; padding: 0; }
  html, body { width: 1200px; height: 1200px; overflow: hidden; }
  body {
    background: var(--bg);
    font-family: "Roboto", Arial, sans-serif;
    color: var(--ink);
    position: relative;
  }
  .sheet-title {
    position: absolute; left: 40px; top: 60px;
    font-size: 22px; letter-spacing: 1px; color: var(--ink);
  }
  .badge {
    position: absolute; top: 280px;
    width: 340px; height: 560px;
    border-radius: 18px; overflow: hidden;
    box-shadow: 0 10px 24px rgba(0,0,0,.18);
  }
  .badge--back { left: 250px; background: var(--card-white); }
  .badge--front { left: 610px; background: var(--card-black); color: #fff; }
  .badge__pattern { position: absolute; inset: 0; width: 100%; height: 100%; }
  .badge__slot {
    position: absolute; top: 22px; left: 50%; transform: translateX(-50%);
    width: 84px; height: 16px; border-radius: 8px; background: var(--slot);
  }
  .badge--front .badge__slot { background: #d8d8d8; }

  /* back */
  .field { position: absolute; left: 26px; right: 30px; }
  .field__label { font-size: 9px; color: var(--ink-soft); text-transform: uppercase; }
  .field__value {
    margin-left: 64px; margin-top: -4px; padding-bottom: 3px;
    font-size: 15px; border-bottom: 1px solid #999;
  }
  .field--name { top: 100px; }
  .field--role { top: 152px; }
  .field--doc { top: 204px; }
  .rules {
    position: absolute; left: 26px; right: 30px; top: 270px;
    list-style: none; font-size: 10.5px; line-height: 1.35; color: var(--ink);
  }
  .rules li { position: relative; padding-left: 12px; margin-bottom: 10px; text-align: justify; }
  .rules li::before { content: "■"; position: absolute; left: 0; font-size: 7px; top: 2px; }
  .brand-mark {
    position: absolute; left: 0; right: 0; top: 410px;
    display: flex; align-items: center; justify-content: center; gap: 10px;
    font-size: 22px; font-weight: 700; letter-spacing: 2px; color: var(--ink);
  }
  .brand-mark__dot { width: 14px; height: 14px; background: var(--accent); }
  .site {
    position: absolute; left: 0; right: 0; bottom: 22px; text-align: center;
    font-size: 13px; letter-spacing: 3px; color: var(--ink);
  }

  /* front */
  .front-brand { position: absolute; left: 0; right: 0; top: 108px; text-align: center; }
  .front-brand__name {
    display: flex; align-items: center; justify-content: center; gap: 10px;
    font-size: 28px; font-weight: 700; letter-spacing: 2px; color: #fff;
  }
  .front-brand__dot { width: 14px; height: 14px; border-radius: 50%; background: var(--accent); }
  .front-brand__tagline { margin-top: 8px; font-size: 12px; color: var(--accent); letter-spacing: 1px; }
  .photo {
    position: absolute; left: 50%; top: 232px; transform: translateX(-50%);
    width: 150px; height: 190px;
    background: linear-gradient(180deg, var(--photo-top) 0%, #b9aa98 55%, var(--photo-bottom) 100%);
  }
  .front-id {
    position: absolute; left: 0; right: 0; bottom: 62px; text-align: center;
    font-size: 16px; letter-spacing: .5px; color: #fff;
  }
</style>
</head>
<body>
  <h1 class="sheet-title">CRACHÁ</h1>

  <section class="badge badge--back" aria-label="Verso do crachá">
    <svg class="badge__pattern" viewBox="0 0 340 560" aria-hidden="true">
      <polygon points="150,0 340,0 340,150 250,150" fill="var(--stripe-light)"/>
      <polygon points="0,230 110,110 150,110 0,270" fill="var(--stripe-light)"/>
      <polygon points="200,240 340,110 340,200 240,290" fill="#f4f4f4"/>
    </svg>
    <div class="badge__slot"></div>

    <div class="field field--name"><div class="field__label">Nome</div><div class="field__value">NOME SOBRENOME</div></div>
    <div class="field field--role"><div class="field__label">Função</div><div class="field__value">ATENDENTE</div></div>
    <div class="field field--doc"><div class="field__label">RG | CPF</div><div class="field__value">00000000000</div></div>

    <ul class="rules">
      <li>Este crachá é pessoal e intransferível, e sua apresentação é indispensável para o ingresso e permanência nas dependências da empresa;</li>
      <li>Em caso de perda ou emergência ocorridas com o seu titular, ligue para (11) 3200-4815</li>
    </ul>

    <div class="brand-mark"><span class="brand-mark__dot"></span>LIVIA PRADO</div>
    <p class="site">www.liviaprado.com.br</p>
  </section>

  <section class="badge badge--front" aria-label="Frente do crachá">
    <svg class="badge__pattern" viewBox="0 0 340 560" aria-hidden="true">
      <polygon points="230,0 340,0 340,90 300,60" fill="var(--stripe-dark)"/>
      <polygon points="0,330 90,250 110,270 0,380" fill="var(--stripe-dark)"/>
      <polygon points="240,330 340,250 340,330 270,390" fill="var(--stripe-dark)"/>
      <polygon points="40,560 170,440 210,440 90,560" fill="#1d1d1d"/>
    </svg>
    <div class="badge__slot"></div>

    <div class="front-brand">
      <div class="front-brand__name"><span class="front-brand__dot"></span>LIVIA PRADO</div>
      <div class="front-brand__tagline">arquitetura e interiores</div>
    </div>

    <div class="photo" role="img" aria-label="Foto do colaborador"></div>

    <p class="front-id">NOME SOBRENOME &nbsp;|&nbsp; FUNÇÃO</p>
  </section>
</body>
</html>
```